need professional, precise design for a website

I will start with a homepage design and if we pick your design, we'll have you design up to 6 more interior pages (we'll pay extra for these of course). We need a homepage design for a reserve study company based in Idaho, covering the northwest region. The company is called copper ridge reserve study. Their current site is at https://www.copperridgereserves.example/ and they really like this site for inspiration https://www.fundplannerhub.example/ but they would like an original design, just more modern and fresh like the sample site. I have logo files I will attach. They want something that looks financial and has a feel of accuity. Their main call to action will be to have someone fill in a contact form or call them on the phone. They will have a sample study that someone can download as on the fundplannerhub site. You can use copy from their current site.

```html
<!DOCTYPE html>
<html lang="en">
<head>
<meta charset="utf-8">
<title>Copper Ridge Reserves — Home</title>
<link rel="stylesheet" href="https://fonts.googleapis.com/css2?family=Montserrat:wght@300;500;600;900&family=Open+Sans:wght@400&display=swap">
<style>
  :root {
    --ink: #111111;
    --nav-ink: #222222;
    --brand-navy: #26285e;
    --accent-yellow: #fbf07a;
    --hero-blue: #3498db;
    --muted: #777777;
    --card-bg: #f7f7f7;
    --footer-bg: #5f5f5f;
    --white: #ffffff;
  }
  * { box-sizing: border-box; margin: 0; padding: 0; }
  html, body { width: 1200px; height: 1200px; overflow: hidden; background: var(--white); }
  body { position: relative; font-family: "Open Sans", sans-serif; }

  .brand { position: absolute; left: 176px; top: 38px; display: flex; align-items: center; gap: 10px; }
  .brand-dot { width: 12px; height: 12px; border-radius: 50%; background: var(--brand-navy); }
  .brand-name { font-family: "Montserrat", sans-serif; font-weight: 500; font-size: 19px; color: var(--brand-navy); letter-spacing: 0.3px; }

  .main-nav { position: absolute; top: 22px; right: 172px; display: flex; align-items: center; }
  .main-nav a { font-family: "Montserrat", sans-serif; font-weight: 500; font-size: 14px; color: var(--nav-ink); text-decoration: none; margin-left: 47px; }
  .main-nav .nav-cta { background: var(--accent-yellow); padding: 10px 10px; border-radius: 18px; font-size: 15px; margin-left: 38px; }

  .hero { position: absolute; left: 98px; top: 84px; width: 1004px; height: 478px; overflow: hidden; }
  .hero-photo { position: absolute; inset: 0; background: linear-gradient(180deg, #f6f6f6 0%, #dadcdc 30%, #9e9c8e 42%, #6f7a4e 58%, #4f6232 78%, #5a6b3c 100%); }
  .hero-panel { position: absolute; left: 162px; top: 142px; width: 259px; height: 242px; background: var(--hero-blue); }
  .hero-panel p { position: absolute; left: 8px; right: 8px; top: 88px; color: var(--white); font-size: 15px; line-height: 18.4px; text-align: center; }
  .hero-title { position: absolute; left: 86px; top: 26px; font-family: "Montserrat", sans-serif; font-weight: 900; font-size: 62px; line-height: 64px; color: var(--ink); letter-spacing: -0.5px; }
  .slide-dots { position: absolute; left: 415px; top: 431px; display: flex; gap: 12px; }
  .slide-dots span { width: 24px; height: 24px; border-radius: 50%; background: var(--white); }
  .slide-dots .is-active { background: #8a8a8a; border: 2px solid var(--white); }

  .offer-title { position: absolute; top: 617px; width: 1200px; text-align: center; font-family: "Montserrat", sans-serif; font-weight: 300; font-size: 31px; color: var(--muted); }
  .offer-card { position: absolute; top: 690px; width: 263px; height: 324px; background: var(--card-bg); border-radius: 6px; box-shadow: 5px 5px 6px rgba(0,0,0,0.18); text-align: center; }
  .offer-card.reporting { left: 324px; }
  .offer-card.focus { left: 618px; }
  .card-label { display: inline-block; margin-top: 32px; background: var(--white); border-radius: 16px; padding: 10px 14px; box-shadow: 3px 3px 5px rgba(0,0,0,0.18); font-family: "Montserrat", sans-serif; font-weight: 600; font-size: 20px; color: #666; }
  .card-list { list-style: none; margin-top: 18px; font-size: 17px; color: var(--muted); }
  .reporting .card-list li { line-height: 34.4px; }
  .focus .card-list li { line-height: 29.2px; }

  .cta-button { position: absolute; left: 534px; top: 1036px; width: 147px; height: 50px; background: var(--accent-yellow); box-shadow: 5px 5px 6px rgba(0,0,0,0.2); border-radius: 3px; display: flex; align-items: center; justify-content: center; font-family: "Montserrat", sans-serif; font-weight: 500; font-size: 24px; color: var(--ink); text-decoration: none; }

  .site-footer { position: absolute; left: 102px; top: 1122px; width: 1000px; height: 78px; background: var(--footer-bg); color: var(--white); font-size: 17px; text-align: center; padding-top: 28px; }
</style>
</head>
<body>
  <header>
    <div class="brand"><span class="brand-dot"></span><span class="brand-name">Copper Ridge Reserves</span></div>
    <nav class="main-nav">
      <a href="#">Home</a>
      <a href="#">About Us</a>
      <a href="#">Services</a>
      <a class="nav-cta" href="#">Contact Us</a>
    </nav>
  </header>

  <section class="hero">
    <div class="hero-photo" role="img" aria-label="Softly blurred city skyline beyond green tree-covered hills under an overcast sky"></div>
    <div class="hero-panel">
      <p>A ridge line is a steady landmark that travelers have relied on for generations. Planning your reserves is simply knowing the right starting points and following a clear map toward the future your community needs.</p>
    </div>
    <h1 class="hero-title">your<br>financial<br>advisory</h1>
    <div class="slide-dots"><span class="is-active"></span><span></span><span></span><span></span><span></span></div>
  </section>

  <h2 class="offer-title">What We Offer</h2>

  <div class="offer-card reporting">
    <div class="card-label">Top Tier Reporting</div>
    <ul class="card-list">
      <li>Expense Forecasting</li>
      <li>Income Projections</li>
      <li>Financial Mapping</li>
      <li>Budget Planning</li>
      <li>Income Consulting</li>
    </ul>
  </div>

  <div class="offer-card focus">
    <div class="card-label">Precision &amp; Focus</div>
    <ul class="card-list">
      <li>Homeowners Associations</li>
      <li>Commercial Property</li>
      <li>Common Area Assets</li>
      <li>Condominiums</li>
      <li>Time Shares</li>
      <li>Apartments</li>
      <li>Parks</li>
    </ul>
  </div>

  <a class="cta-button" href="#">Contact Us</a>

  <footer class="site-footer">© 2019 All Rights Reserved</footer>
</body>
</html>
```